Steadfast Support! Virtual Assistant business needs a Website

I have started an online business called "Steadfast Support". I offer all the same types of services as a typical Personal Assistant, only remotely. For example, document formatting and editing (word, powerpoint, excel etc.), email and calendar management, appointments and bookings, document creation, reports, travel and event management and so on.

I already have a logo ready to go, however I have yet to finalise the copy for the site, so if you could create the pages with pictures, and I can fill in the wording at a later date.

Target Market(s)

Anyone who is overloaded at work and needs someone to take the admin work off their hands.

Number of Pages Required

4 page

Font styles to use
Sans Serif
Script
Other font styles liked:
• Gotham Medium is used in my font

Colors

Designer to choose colors to be used in the design.

Requirements
Must have
• Home Page
• About Page
• Pricing Page
• Contact Page
Nice to have
• Pictures and a professional design, I like white space and simple design.
Should not have
• cartoons or anything unprofessional looking.

```html
<!DOCTYPE html>
<html lang="en">
<head>
<meta charset="utf-8">
<title>Steadfast Support</title>
<link href="https://fonts.googleapis.com/css2?family=Montserrat:wght@400;500;600;700&family=Open+Sans:ital,wght@0,400;0,600;0,700;1,400&display=swap" rel="stylesheet">
<style>
:root{
  --navy:#1b3a8c;
  --blue:#1a57b8;
  --blue-deep:#0d47a8;
  --blue-light:#2f7fd6;
  --orange:#f47b20;
  --ink:#333a44;
  --muted:#6b7280;
  --line:#e3e6ea;
  --grey-band:#878787;
  --footer:#2b2b2b;
  --white:#ffffff;
}
*{margin:0;padding:0;box-sizing:border-box}
html,body{width:1200px;height:4128px;overflow:hidden}
body{position:relative;background:var(--white);font-family:'Open Sans',Arial,sans-serif;color:var(--ink)}
.abs{position:absolute}
.heading{font-family:'Montserrat',Arial,sans-serif;font-weight:700;color:var(--navy);letter-spacing:1px;text-align:center;font-size:20px}
.rule{width:60px;height:2px;background:#c8ccd2;margin:14px auto 0}

/* hero */
.hero{left:0;top:0;width:1200px;height:592px;background:linear-gradient(100deg,#dfe3e4 0%,#eef0ef 35%,#c9c2b8 55%,#e6e7e6 75%,#d2d6d8 100%)}
.brand{left:132px;top:30px;display:flex;align-items:center;gap:14px}
.brand-dot{width:58px;height:58px;border-radius:50%;background:var(--navy)}
.brand-name{font-family:'Montserrat',sans-serif;font-weight:600;font-size:24px;color:var(--navy);letter-spacing:1px}
.nav{right:70px;top:25px;display:flex;gap:30px;font-family:'Montserrat',sans-serif;font-weight:600;font-size:12px;color:var(--navy);letter-spacing:.5px}
.nav a{color:inherit;text-decoration:none;padding:5px 10px}
.nav a.active{background:var(--navy);color:var(--white)}
.hero-band{left:730px;top:132px;width:470px;height:102px;background:rgba(255,255,255,.55);padding:20px 0 0 28px}
.hero-title{font-family:'Montserrat',sans-serif;font-weight:700;font-size:32px;color:var(--navy);letter-spacing:.5px}
.hero-sub{font-weight:600;font-size:15px;color:var(--navy);margin-top:2px}
.dots{left:552px;top:518px;display:flex;gap:14px}
.dots span{width:9px;height:9px;border-radius:50%;background:rgba(255,255,255,.8)}
.dots span.on{background:var(--white);box-shadow:0 0 0 2px rgba(27,58,140,.4)}

/* services */
.services-title{left:0;top:652px;width:1200px}
.service-grid{left:130px;top:740px;width:943px;height:560px;display:grid;grid-template-columns:repeat(4,1fr);grid-template-rows:278px 282px}
.service{text-align:center;padding:40px 18px 0;border-right:1px solid var(--line)}
.service:nth-child(4n){border-right:none}
.service:nth-child(-n+4){border-bottom:1px solid var(--line)}
.service svg{width:56px;height:56px;fill:var(--blue)}
.service h3{font-family:'Montserrat',sans-serif;font-weight:600;font-size:15px;color:#222;margin:18px 0 12px;line-height:1.35}
.service p{font-size:11px;line-height:1.5;color:var(--muted);padding:0 8px}

/* welcome */
.welcome{left:0;top:1321px;width:1200px;height:540px;background:linear-gradient(90deg,#f1ebe3 0%,#e9dfd1 45%,#d9c6ac 70%,#cdb699 100%)}
.welcome-mark{left:140px;top:1402px;width:96px;height:96px;border-radius:50%;background:var(--navy)}
.welcome-kicker{left:262px;top:1414px;font-family:'Montserrat',sans-serif;font-weight:600;font-size:16px;color:var(--navy)}
.welcome-name{left:262px;top:1436px;font-family:'Montserrat',sans-serif;font-weight:700;font-size:26px;color:var(--blue)}
.welcome-rule{left:262px;top:1480px;width:330px;height:1px;background:#8a8f98}
.welcome-text{left:262px;top:1502px;width:340px;font-size:12.5px;line-height:20px;color:#444;text-align:justify}
.btn-navy{left:267px;top:1684px;width:110px;height:31px;background:var(--navy);color:var(--white);font-family:'Montserrat',sans-serif;font-weight:700;font-size:11px;letter-spacing:.5px;display:flex;align-items:center;justify-content:center}

/* pricing */
.pricing-bg{left:0;top:1760px}
.pricing-title{left:0;top:1884px;width:1200px;color:var(--white)}
.plan{text-align:center;color:var(--white)}
.plan-side{top:2006px;width:258px;height:330px;background:rgba(120,180,240,.35);padding-top:28px}
.plan-name{font-family:'Montserrat',sans-serif;font-size:14px;letter-spacing:1px}
.price{font-family:'Montserrat',sans-serif;font-weight:500;font-size:44px;line-height:1;margin:8px 0 18px;display:flex;justify-content:center;align-items:flex-start}
.price small{font-size:20px;margin-top:4px}
.price sub{font-size:22px;vertical-align:baseline;align-self:flex-end;margin-bottom:2px}
.features{list-style:none;font-size:12px;margin:0 22px}
.features li{padding:10px 0;border-bottom:1px solid rgba(255,255,255,.35)}
.features li:last-child{border-bottom:none}
.btn-outline{display:inline-block;margin-top:12px;width:132px;padding:7px 0;border:2px solid var(--white);font-size:11px;font-weight:600}
.plan-feature{left:460px;top:1957px;width:305px;height:426px;background:var(--white);color:var(--ink);box-shadow:0 10px 30px rgba(0,0,0,.25)}
.plan-feature .plan-head{height:46px;background:var(--orange);color:var(--white);font-family:'Montserrat',sans-serif;font-size:16px;letter-spacing:1px;display:flex;align-items:center;justify-content:center}
.plan-feature .price{font-size:56px;color:#222;margin:26px 0 18px}
.plan-feature .price small{font-size:26px}
.plan-feature .price sub{font-size:28px}
.plan-feature .features{font-size:14px;margin:0 34px}
.plan-feature .features li{padding:12px 0;border-bottom:1px solid #d7d7d7}
.plan-feature .features li:last-child{border-bottom:none}
.btn-orange{display:inline-block;margin-top:16px;width:160px;padding:10px 0;background:var(--orange);color:var(--white);font-size:13px;font-weight:600;box-shadow:0 3px 6px rgba(0,0,0,.2)}

/* contact */
.contact-bg{left:0;top:2440px;width:1200px;height:587px;background:linear-gradient(160deg,#ffffff 0%,#f6f7f8 50%,#eceef0 100%)}
.contact-title{left:0;top:2553px;width:1200px}
.field-label{font-size:13px;color:#444}
.field{background:#eef0f2;border:1px solid #cfd3d8}
.btn-blue{left:512px;top:2917px;width:176px;height:40px;background:linear-gradient(#2e6cc6,#1a4f9e);color:var(--white);font-size:14px;font-weight:600;display:flex;align-items:center;justify-content:center;box-shadow:0 3px 6px rgba(0,0,0,.2)}

/* testimonials */
.testimonials{left:0;top:3027px;width:1200px;height:509px;background:var(--grey-band)}
.testimonials-title{left:0;top:3118px;width:1200px;color:var(--white);font-weight:500;font-size:28px;letter-spacing:2px}
.quote{top:3264px;width:286px;height:182px;border:2px solid rgba(255,255,255,.85);color:var(--white);text-align:center;padding:62px 22px 0}
.quote p{font-style:italic;font-size:11.5px;line-height:1.55}
.quote h4{font-weight:700;font-size:16px;margin-top:14px}
.avatar{top:3222px;width:78px;height:78px;border-radius:50%;border:3px solid var(--white);background:linear-gradient(#c9b59d,#8f7a66)}
.arrow{top:3337px;width:36px;height:36px;border-radius:50%;background:#d0d0d0;display:flex;align-items:center;justify-content:center}

/* partners */
.partners-title{left:0;top:3612px;width:1200px}
.partner-box{left:212px;top:3688px;width:770px;height:137px;border:1px solid #e6e6e6;display:flex;align-items:center;justify-content:space-around;padding:0 40px}
.partner-badge{width:120px;height:40px;border-radius:6px;background:#c9ccd0}

/* footer */
.footer{left:0;top:3955px;width:1200px;height:173px;background:var(--footer);color:var(--white)}
.footer-mark{left:561px;top:3922px;width:66px;height:66px;border-radius:50%;background:var(--blue);border:3px solid var(--white)}
.footer-name{left:0;top:4024px;width:1200px;text-align:center;font-family:'Montserrat',sans-serif;font-weight:600;font-size:24px;letter-spacing:1.5px}
.footer-nav{left:138px;top:4016px;display:flex;gap:26px;font-family:'Montserrat',sans-serif;font-size:11px;font-weight:600}
.footer-copy{left:138px;top:4060px;font-size:10.5px;line-height:1.5;color:#cfcfcf}
.follow{left:908px;top:4014px;font-family:'Montserrat',sans-serif;font-size:12px;font-weight:600;letter-spacing:.5px}
.social{left:910px;top:4050px;display:flex;gap:20px}
.social span{width:20px;height:20px;border-radius:50%;background:var(--white)}
</style>
</head>
<body>

<!-- hero -->
<div class="abs hero" role="img" aria-label="Photo of a professional woman working on a laptop in a bright office"></div>
<div class="abs brand"><span class="brand-dot"></span><span class="brand-name">STEADFAST SUPPORT</span></div>
<nav class="abs nav"><a class="active">HOME</a><a>ABOUT US</a><a>PRICING</a><a>CONTACT US</a></nav>
<div class="abs hero-band">
  <div class="hero-title">ONLINE BUSINESS</div>
  <div class="hero-sub">Lorem Ipsum is simply dummy text of the</div>
</div>
<div class="abs dots"><span></span><span class="on"></span><span></span><span></span><span></span></div>

<!-- services -->
<div class="abs services-title heading">OUR SERVICES<div class="rule"></div></div>
<div class="abs service-grid">
  <div class="service">
    <svg viewBox="0 0 56 56"><circle cx="28" cy="15" r="11"/><path d="M6 54c0-14 10-24 22-24s22 10 22 24z"/></svg>
    <h3>Personal Assistant</h3>
    <p>Sed ut perspiciatis unde omnis iste natus error sit voluptatem accu santium doloremque laudantium, totam rem aperiam.</p>
  </div>
  <div class="service">
    <svg viewBox="0 0 56 56"><rect x="6" y="6" width="44" height="7"/><rect x="6" y="19" width="30" height="5"/><rect x="6" y="30" width="44" height="7"/><rect x="6" y="43" width="30" height="5"/></svg>
    <h3>Document formatting<br>and editing</h3>
    <p>Sed ut perspiciatis unde omnis iste natus error sit voluptatem accu santium doloremque.</p>
  </div>
  <div class="service">
    <svg viewBox="0 0 56 56"><circle cx="28" cy="16" r="10"/><path d="M14 16a14 14 0 0 1 28 0" fill="none" stroke="#1a57b8" stroke-width="3"/><rect x="8" y="30" width="40" height="24" rx="3"/></svg>
    <h3>Email and calendar<br>Management</h3>
    <p>Sed ut perspiciatis unde omnis iste natus error sit voluptatem accu santium doloremque.</p>
  </div>
  <div class="service">
    <svg viewBox="0 0 56 56"><path d="M6 10h44v42H6z M10 22v26h36V22z" fill-rule="evenodd"/><rect x="14" y="4" width="4" height="10"/><rect x="38" y="4" width="4" height="10"/><rect x="14" y="26" width="6" height="5"/><rect x="25" y="26" width="6" height="5"/><rect x="36" y="26" width="6" height="5"/><rect x="14" y="36" width="6" height="5"/><rect x="25" y="36" width="6" height="5"/></svg>
    <h3>Appointments and<br>Bookings</h3>
    <p>Sed ut perspiciatis unde omnis iste natus error sit voluptatem accu santium doloremque.</p>
  </div>
  <div class="service">
    <svg viewBox="0 0 56 56"><rect x="14" y="4" width="36" height="44" rx="2"/><rect x="6" y="10" width="36" height="44" rx="2" stroke="#fff" stroke-width="2"/><rect x="12" y="20" width="24" height="3" fill="#fff"/><rect x="12" y="28" width="24" height="3" fill="#fff"/><rect x="12" y="36" width="18" height="3" fill="#fff"/></svg>
    <h3>Document creation</h3>
    <p>Sed ut perspiciatis unde omnis iste natus error sit voluptatem accu santium doloremque laudantium, totam rem aperiam.</p>
  </div>
  <div class="service">
    <svg viewBox="0 0 56 56"><rect x="10" y="4" width="36" height="48" rx="3"/><circle cx="28" cy="22" r="7" fill="#fff"/><rect x="16" y="36" width="24" height="3" fill="#fff"/><rect x="16" y="42" width="24" height="3" fill="#fff"/></svg>
    <h3>Reports</h3>
    <p>Sed ut perspiciatis unde omnis iste natus error sit voluptatem accu santium doloremque laudantium, totam rem aperiam.</p>
  </div>
  <div class="service">
    <svg viewBox="0 0 56 56"><path d="M20 14V8h16v6h-4v-3h-8v3z"/><rect x="4" y="14" width="48" height="36" rx="4"/><rect x="14" y="14" width="3" height="36" fill="#fff"/><rect x="39" y="14" width="3" height="36" fill="#fff"/></svg>
    <h3>Travel Management</h3>
    <p>Sed ut perspiciatis unde omnis iste natus error sit voluptatem accu santium doloremque laudantium, totam rem aperiam.</p>
  </div>
  <div class="service">
    <svg viewBox="0 0 56 56"><circle cx="22" cy="14" r="10"/><path d="M2 50c0-13 9-22 20-22 4 0 7 1 10 3v19z"/><circle cx="40" cy="40" r="13"/><path d="M40 32v9h7" fill="none" stroke="#fff" stroke-width="3"/></svg>
    <h3>Event Management</h3>
    <p>Sed ut perspiciatis unde omnis iste natus error sit voluptatem accu santium doloremque laudantium, totam rem aperiam.</p>
  </div>
</div>

<!-- welcome -->
<div class="abs welcome" role="img" aria-label="Photo of hands writing in a notebook beside a laptop and glasses on a light wooden desk"></div>
<div class="abs welcome-mark"></div>
<div class="abs welcome-kicker">WELCOME TO</div>
<div class="abs welcome-name">STEADFAST SUPPORT</div>
<div class="abs welcome-rule"></div>
<p class="abs welcome-text">At vero eos et accusamus et iusto odio dignissimos ducimus qui blanditiis praesentium voluptatum deleniti atque corrupti quos dolores et quas molestias excepturi sint occaecati cupiditate non provident, similique sunt in culpa qui officia deserunt mollitia animi, id est laborum et dolorum fuga. Et harum quidem rerum facilis est et expedita distinctio. Nam libero tempore.</p>
<div class="abs btn-navy">READ MORE</div>

<!-- pricing -->
<svg class="abs pricing-bg" width="1200" height="740" viewBox="0 0 1200 740">
  <defs><linearGradient id="priceGrad" x1="0" y1="0" x2="1" y2="1"><stop offset="0" stop-color="#2f7fd6"/><stop offset="1" stop-color="#0d47a8"/></linearGradient></defs>
  <polygon points="0,90 1200,29 1200,600 0,735" fill="url(#priceGrad)"/>
  <polygon points="0,62 600,70 0,90" fill="#b9bcc2" opacity=".6"/>
</svg>
<div class="abs pricing-title heading" style="color:#fff">PRICING</div>

<div class="abs plan plan-side" style="left:217px">
  <div class="plan-name">BASIC</div>
  <div class="price"><small>$</small>30<sub>.00</sub></div>
  <ul class="features"><li>Morbi diam mauris</li><li>Aiverra in gravida eu</li><li>Mattis in ante Morbi</li><li>Eget arcu Morbi</li></ul>
  <span class="btn-outline">CLICK HERE</span>
</div>
<div class="abs plan plan-side" style="left:765px">
  <div class="plan-name">PREMIUM</div>
  <div class="price"><small>$</small>90<sub>.00</sub></div>
  <ul class="features"><li>Morbi diam mauris</li><li>Aiverra in gravida eu</li><li>Mattis in ante Morbi</li><li>Eget arcu Morbi</li></ul>
  <span class="btn-outline">CLICK HERE</span>
</div>
<div class="abs plan plan-feature">
  <div class="plan-head">STANDARD</div>
  <div class="price"><small>$</small>45<sub>.00</sub></div>
  <ul class="features"><li>Morbi diam mauris</li><li>Aiverra in gravida eu</li><li>Mattis in ante Morbi</li><li>Eget arcu Morbi</li></ul>
  <span class="btn-orange">CLICK HERE</span>
</div>

<!-- contact -->
<div class="abs contact-bg" role="img" aria-label="Photo of a white desk with keyboard, pen, notebook and mouse" style="z-index:-1"></div>
<div class="abs contact-title heading">CONTACT US</div>
<label class="abs field-label" style="left:182px;top:2664px">Your Name</label>
<label class="abs field-label" style="left:475px;top:2664px">Email address</label>
<label class="abs field-label" style="left:765px;top:2664px">Phone Number</label>
<div class="abs field" style="left:182px;top:2694px;width:281px;height:42px"></div>
<div class="abs field" style="left:473px;top:2694px;width:281px;height:42px"></div>
<div class="abs field" style="left:765px;top:2694px;width:281px;height:42px"></div>
<label class="abs field-label" style="left:185px;top:2748px">Message</label>
<div class="abs field" style="left:182px;top:2777px;width:864px;height:113px"></div>
<div class="abs btn-blue">CLICK HERE</div>

<!-- testimonials -->
<div class="abs testimonials"></div>
<div class="abs testimonials-title heading">TESTIMONIALS</div>
<div class="abs arrow" style="left:67px"><svg width="12" height="12" viewBox="0 0 12 12"><path d="M8 1L3 6l5 5" fill="none" stroke="#666" stroke-width="2"/></svg></div>
<div class="abs arrow" style="left:1094px"><svg width="12" height="12" viewBox="0 0 12 12"><path d="M4 1l5 5-5 5" fill="none" stroke="#666" stroke-width="2"/></svg></div>

<div class="abs quote" style="left:132px"><p>Nam libero tempore, cum soluta nobis est eligendi optio cumque nihil impedit quo minus id quod maxime placea</p><h4>Clara Wendt</h4></div>
<div class="abs quote" style="left:457px"><p>Nam libero tempore, cum soluta nobis est eligendi optio cumque nihil impedit quo minus id quod maxime placea</p><h4>Nina Forsby</h4></div>
<div class="abs quote" style="left:782px"><p>Nam libero tempore, cum soluta nobis est eligendi optio cumque nihil impedit quo minus id quod maxime placea</p><h4>Owen Marsh</h4></div>
<div class="abs avatar" style="left:236px" role="img" aria-label="Portrait photo of Clara Wendt"></div>
<div class="abs avatar" style="left:561px" role="img" aria-label="Portrait photo of Nina Forsby"></div>
<div class="abs avatar" style="left:886px" role="img" aria-label="Portrait photo of Owen Marsh"></div>

<!-- partners -->
<div class="abs partners-title heading">OUR PARTNERS</div>
<div class="abs partner-box">
  <span class="partner-badge"></span><span class="partner-badge"></span><span class="partner-badge"></span><span class="partner-badge"></span>
</div>

<!-- footer -->
<footer class="abs footer"></footer>
<div class="abs footer-mark"></div>
<div class="abs footer-name" style="color:#fff">STEADFAST SUPPORT</div>
<nav class="abs footer-nav" style="color:#fff"><span>HOME</span><span>ABOUT US</span><span>PRICING</span><span>CONTACT US</span></nav>
<div class="abs footer-copy">Copyright© 2016 Company Name<br>Rights Reserved</div>
<div class="abs follow" style="color:#fff">FOLLOW US</div>
<div class="abs social"><span></span><span></span><span></span><span></span></div>

</body>
</html>
```